Pamphlet for IT Services Company (MSP Provider or Managed Services Provider)

We need a pamphlet designed for our Managed Services Company. We are an established company of 17 years that has never advertised. We'd like a pamphlet that we can drop off at potential client sites that describes our services. I like clean and prefer Orange as an accent color. We'd like to touch on the fact that we cater to our clients needs and go above and beyond what the other providers do.

Target Market(s)

Small and Medium Sized Businesses

Industry/Entity Type

It Service

Font styles to use
Other font styles liked:
• Try to match font on logo or website

Requirements
Must have
• Must highlight with the following Services and descriptions with Logo
Managed IT Services
IT Support
VOIP Solutions
WiFI Solutions
Contact information with phone number and website address.
Please view website korvantech.com
try to match fons on website above.
Nice to have
• Customer Testimonials. May a couple one line testimonials. Not real sure because this is the first time we've ever designed a brochure.
Should not have
• Not Sure

```html
<!DOCTYPE html>
<html lang="en">
<head>
<meta charset="utf-8">
<title>Korvan Technologies – Managed Services Plan</title>
<link rel="stylesheet" href="https://fonts.googleapis.com/css2?family=Montserrat:wght@400;500;600;700;800;900&display=swap">
<style>
  :root {
    --orange: #f28a30;
    --orange-deep: #ee7a1c;
    --cream: #fbecd5;
    --navy: #1c2838;
    --ink: #1d1d1f;
    --slate: #5b6673;
    --body: #3a3a3a;
    --paper: #ffffff;
    --canvas: #efefef;
    --photo-deep: #071a3c;
    --photo-mid: #0d4d8c;
    --photo-glow: #37a9e6;
    --badge: #d9dadc;
  }
  * { margin: 0; padding: 0; box-sizing: border-box; }
  html, body { width: 1200px; height: 2297px; overflow: hidden; background: var(--canvas); }
  body { position: relative; font-family: "Montserrat", sans-serif; color: var(--ink); }

  .spread {
    position: absolute; left: 40px; width: 888px; height: 628px;
    background: var(--paper); transform: scale(1.2613); transform-origin: 0 0;
    box-shadow: 0 3px 8px rgba(0,0,0,.18); overflow: hidden;
  }
  .spread--outside { top: 306px; }
  .spread--inside { top: 1198px; }
  .spread-art { position: absolute; inset: 0; width: 888px; height: 628px; }
  .abs { position: absolute; }

  /* outside: stats panel */
  .stats { left: 0; top: 48px; width: 296px; text-align: center; }
  .stat { margin-bottom: 34px; }
  .stat-value { font-weight: 900; line-height: 1; letter-spacing: -1px; }
  .stat-label { font-size: 12px; font-weight: 500; margin-top: 6px; color: var(--ink); }
  .stat--slate .stat-value { color: var(--slate); font-size: 46px; }
  .stat--dark .stat-value { color: var(--ink); font-size: 50px; }
  .stat--orange .stat-value { color: var(--orange); font-size: 46px; }
  .stat--big .stat-value { color: var(--ink); font-size: 54px; }

  .brand { display: flex; align-items: center; gap: 6px; color: var(--orange); font-weight: 500; }
  .brand-dot { width: 14px; height: 14px; border-radius: 50%; background: var(--orange); }
  .brand--top { right: 36px; top: 42px; font-size: 20px; }
  .brand--contact { left: 296px; width: 296px; top: 432px; justify-content: center; font-size: 17px; }

  .contact { left: 296px; width: 296px; top: 462px; text-align: center; font-size: 7.5px; font-weight: 600; line-height: 1.25; color: var(--ink); }
  .contact-item { margin-bottom: 9px; }
  .contact-icon { display: block; margin: 0 auto 3px; }
  .contact-phone { font-size: 9px; }

  .cover-title { left: 592px; width: 296px; top: 478px; text-align: center; line-height: .92; }
  .cover-title span { display: block; }
  .cover-title .line-1 { font-size: 34px; font-weight: 500; color: var(--ink); letter-spacing: 1px; }
  .cover-title .line-2 { font-size: 37px; font-weight: 900; color: var(--orange); }
  .cover-title .line-3 { font-size: 37px; font-weight: 900; color: var(--orange); }
  .cover-url { left: 592px; width: 296px; top: 595px; text-align: center; font-size: 14px; font-weight: 600; color: var(--ink); }
  .cover-url em { font-style: normal; color: var(--orange); }

  /* inside: services */
  .service { width: 232px; }
  .service-head { display: flex; align-items: center; gap: 12px; margin-bottom: 14px; }
  .service-title { font-size: 14px; font-weight: 500; line-height: 1.15; color: var(--ink); }
  .service-title b { color: var(--orange); font-weight: 800; }
  .service-text { font-size: 10.8px; line-height: 1.38; color: var(--body); text-align: justify; }

  .partners-pill {
    left: 638px; top: 378px; width: 204px; height: 34px; border-radius: 17px;
    background: var(--orange); color: #fff; font-weight: 800; font-size: 17px;
    display: flex; align-items: center; justify-content: center; letter-spacing: .3px;
    box-shadow: 0 3px 4px rgba(0,0,0,.2);
  }
  .partner-badge { position: absolute; background: var(--badge); }
</style>
</head>
<body>

<!-- Outside spread: stats / contact / cover -->
<section class="spread spread--outside">
  <svg class="spread-art" viewBox="0 0 888 628" xmlns="http://www.w3.org/2000/svg">
    <defs>
      <linearGradient id="cloudPhoto" x1="0" y1="0" x2="1" y2="1">
        <stop offset="0" stop-color="#050f24"/>
        <stop offset=".45" stop-color="#0c3f7a"/>
        <stop offset=".7" stop-color="#2a8fd6"/>
        <stop offset="1" stop-color="#0a1e3d"/>
      </linearGradient>
      <radialGradient id="globePhoto" cx=".5" cy=".45" r=".6">
        <stop offset="0" stop-color="#48b8ef"/>
        <stop offset=".6" stop-color="#0d4d8c"/>
        <stop offset="1" stop-color="#071a3c"/>
      </radialGradient>
      <linearGradient id="laptopPhoto" x1="0" y1="0" x2="1" y2="1">
        <stop offset="0" stop-color="#2c3440"/>
        <stop offset=".5" stop-color="#8fa3b8"/>
        <stop offset="1" stop-color="#c9ced4"/>
      </linearGradient>
    </defs>
    <path d="M380,0 H888 V92 C760,96 610,70 470,22 C440,12 410,4 380,0 Z" fill="var(--cream)"/>
    <path d="M0,0 H380 C440,6 500,28 560,50 C680,90 780,100 888,92 V132 C720,150 520,95 400,62 C300,36 200,22 0,42 Z" fill="var(--orange)"/>
    <path role="img" aria-label="Photo: hands on a laptop beneath a glowing digital cloud over a blue globe"
          d="M296,42 C420,60 560,118 700,135 C780,142 840,138 888,132 V392 C800,420 700,410 600,378 C520,352 420,340 296,345 Z"
          fill="url(#cloudPhoto)"/>
    <path d="M520,350 C620,392 760,425 888,392 V455 C780,470 660,445 560,395 C540,384 528,370 520,350 Z" fill="var(--navy)"/>
    <path d="M530,362 C640,410 770,432 888,404" fill="none" stroke="var(--orange)" stroke-width="6"/>
    <circle cx="444" cy="340" r="80" fill="var(--orange)"/>
    <circle role="img" aria-label="Photo: holographic network icons above a tablet" cx="444" cy="340" r="74" fill="url(#globePhoto)"/>
    <rect role="img" aria-label="Photo: laptop showing an analytics dashboard" x="14" y="475" width="270" height="125" rx="6" fill="url(#laptopPhoto)"/>
  </svg>

  <div class="abs brand brand--top"><span class="brand-dot"></span>korvan technologies</div>

  <div class="abs stats">
    <div class="stat stat--slate"><div class="stat-value">45+</div><div class="stat-label">Happy MSP Clients</div></div>
    <div class="stat stat--dark"><div class="stat-value">700+</div><div class="stat-label">Protected Endpoints</div></div>
    <div class="stat stat--orange"><div class="stat-value">50+</div><div class="stat-label">Protected Networks</div></div>
    <div class="stat stat--big"><div class="stat-value">500TB+</div><div class="stat-label">Terabytes of Encrypted Backups</div></div>
  </div>

  <div class="abs brand brand--contact"><span class="brand-dot"></span>korvan technologies</div>

  <div class="abs contact">
    <div class="contact-item">
      <svg class="contact-icon" width="8" height="10" viewBox="0 0 8 10"><path d="M4,0 A3.5,3.5 0 0 1 7.5,3.5 C7.5,6 4,10 4,10 C4,10 .5,6 .5,3.5 A3.5,3.5 0 0 1 4,0 Z" fill="var(--orange)"/><circle cx="4" cy="3.5" r="1.3" fill="#fff"/></svg>
      PO Box 402<br>Millbrook MO 63100<br>United States
    </div>
    <div class="contact-item contact-phone">
      <svg class="contact-icon" width="9" height="9" viewBox="0 0 10 10"><path d="M2,0 L4,2.5 L3,3.8 C3.8,5.4 4.6,6.2 6.2,7 L7.5,6 L10,8 L8.5,10 C4,9.5 .5,6 0,1.5 Z" fill="var(--orange)"/></svg>
      +1 (555) 014-2290
    </div>
    <div class="contact-item">
      <svg class="contact-icon" width="10" height="7" viewBox="0 0 10 7"><rect width="10" height="7" fill="var(--orange)"/><path d="M0,0 L5,4 L10,0" fill="none" stroke="#fff" stroke-width="1"/></svg>
      hello@korvantech.com
    </div>
    <div class="contact-item">
      <svg class="contact-icon" width="9" height="9" viewBox="0 0 10 10"><circle cx="5" cy="5" r="4.5" fill="none" stroke="var(--orange)" stroke-width="1.2"/><path d="M.5,5 H9.5 M5,.5 C2,3 2,7 5,9.5 M5,.5 C8,3 8,7 5,9.5" fill="none" stroke="var(--orange)" stroke-width="1"/></svg>
      www.korvantech.com
    </div>
  </div>

  <h1 class="abs cover-title">
    <span class="line-1">MANAGED</span>
    <span class="line-2">SERVICES</span>
    <span class="line-3">PLAN</span>
  </h1>
  <div class="abs cover-url">www.<em>korvantech</em>.com</div>
</section>

<!-- Inside spread: services / partners -->
<section class="spread spread--inside">
  <svg class="spread-art" viewBox="0 0 888 628" xmlns="http://www.w3.org/2000/svg">
    <defs>
      <linearGradient id="businessPhoto" x1="0" y1="0" x2="1" y2="1">
        <stop offset="0" stop-color="#1a2a44"/>
        <stop offset=".5" stop-color="#3d7fb8"/>
        <stop offset="1" stop-color="#0c1b33"/>
      </linearGradient>
      <linearGradient id="serverPhoto" x1="0" y1="0" x2="1" y2="0">
        <stop offset="0" stop-color="#06203f"/>
        <stop offset=".5" stop-color="#2b7dc0"/>
        <stop offset="1" stop-color="#061a36"/>
      </linearGradient>
    </defs>
    <path d="M0,0 H592 C520,12 470,20 400,24 C260,32 120,16 0,38 Z" fill="var(--orange)"/>
    <path d="M380,26 C470,22 540,12 592,0" fill="none" stroke="var(--navy)" stroke-width="3"/>

    <path role="img" aria-label="Photo: businessman touching a digital globe with data overlays"
          d="M592,0 H888 V292 C800,345 680,335 592,300 Z" fill="url(#businessPhoto)"/>
    <path d="M592,300 C680,335 800,345 888,292 V312 C800,368 680,352 592,322 Z" fill="var(--orange)"/>

    <path d="M0,345 C130,318 280,345 400,362 C480,372 545,360 592,340 V628 H0 Z" fill="var(--cream)"/>
    <path d="M0,365 C130,335 290,360 410,378 C490,388 550,372 592,352 V395 C550,420 480,432 400,420 C280,402 130,380 0,405 Z" fill="var(--orange)"/>
    <path role="img" aria-label="Photo: glowing server racks in a data centre corridor"
          d="M0,405 C130,380 280,402 400,420 C480,432 550,420 592,395 V628 H0 Z" fill="url(#serverPhoto)"/>

    <line x1="740" y1="445" x2="740" y2="580" stroke="#9a9a9a" stroke-width="1"/>
  </svg>

  <!-- Managed IT -->
  <div class="abs service" style="left:30px;top:38px;">
    <div class="service-head">
      <svg width="30" height="30" viewBox="0 0 30 30" fill="none" stroke="var(--ink)" stroke-width="1.6">
        <rect x="4" y="6" width="22" height="16" rx="1.5"/><path d="M1,26 H29"/><path d="M12,11 L9,14 L12,17 M18,11 L21,14 L18,17 M16,10 L14,18"/>
      </svg>
      <div class="service-title">LET US TAKE<br><b>CARE OF YOUR IT</b></div>
    </div>
    <p class="service-text">Our MSP is a Flat Rate service that includes Onsite &amp; Remote Support, Endpoint Protection, Web Filtering, Encrypted Online Backup &amp; Patch Management</p>
  </div>

  <!-- VOIP -->
  <div class="abs service" style="left:30px;top:176px;">
    <div class="service-head">
      <svg width="34" height="30" viewBox="0 0 34 30" fill="none" stroke="var(--ink)" stroke-width="1.6">
        <path d="M4,6 L8,4 L11,11 L8,13 C9,17 12,20 16,22 L18,19 L25,22 L23,26 C12,26 4,18 4,6 Z"/><rect x="16" y="2" width="16" height="10" rx="5"/>
      </svg>
      <div class="service-title">VOIP <b>SOLUTIONS</b></div>
    </div>
    <p class="service-text">Phones are more than just an attachment to a desk. Allow us to help you maximize communication with your team and customers by using the latest technology that will likely save you money as well. Korvan Technologies partners with Relaywave to provide phone hardware, systems, and phone service</p>
  </div>

  <!-- IT Support -->
  <div class="abs service" style="left:294px;top:40px;">
    <div class="service-head">
      <svg width="32" height="32" viewBox="0 0 32 32" fill="none" stroke="var(--ink)" stroke-width="1.6">
        <circle cx="19" cy="10" r="5"/><circle cx="19" cy="10" r="8" stroke-dasharray="3 2"/><path d="M2,24 H9 L14,22 H20 C22,22 22,25 20,25 H14 M9,29 H20 L29,22"/>
      </svg>
      <div class="service-title">IT <b>SUPPORT</b></div>
    </div>
    <p class="service-text">We have a passion for what we do and it shows! Korvan provides fast, reliable, expert solutions from experienced staff. You will never feel like just another client to us because our customers are family!</p>
  </div>

  <!-- WiFi -->
  <div class="abs service" style="left:294px;top:192px;">
    <div class="service-head">
      <svg width="32" height="26" viewBox="0 0 32 26" fill="none" stroke="var(--ink)" stroke-width="2.2" stroke-linecap="round">
        <path d="M2,9 C10,1 22,1 30,9"/><path d="M7,14 C12,9 20,9 25,14"/><path d="M12,19 C14,17 18,17 20,19"/><circle cx="16" cy="23" r="1.5" fill="var(--ink)"/>
      </svg>
      <div class="service-title">WIFI <b>SOLUTIONS</b></div>
    </div>
    <p class="service-text">WiFi is everywhere! (At least it should be.) Korvan can extend your WiFi to cover your whole campus</p>
  </div>

  <div class="abs partners-pill">OUR PARTNERS</div>

  <div class="partner-badge" style="left:634px;top:448px;width:74px;height:20px;border-radius:2px;"></div>
  <div class="partner-badge" style="left:772px;top:452px;width:76px;height:12px;border-radius:2px;"></div>
  <div class="partner-badge" style="left:628px;top:498px;width:80px;height:22px;background:#4a4a4a;border-radius:2px;"></div>
  <div class="partner-badge" style="left:770px;top:500px;width:82px;height:16px;border-radius:2px;"></div>
  <div class="partner-badge" style="left:654px;top:556px;width:26px;height:26px;border-radius:50%;"></div>
  <div class="partner-badge" style="left:796px;top:552px;width:26px;height:26px;border-radius:4px;"></div>
</section>

</body>
</html>
```